Satchel & Compass needs new business card design

I need a new business card design. I'm looking for out-of-the-box design which represents the freedom of being a location independent entrepreneur.
I offer coaching, retreats and trips.
I would like to see designs with and without the photo.
Colors I use are black (#000000), green (#25A796) and brown (#D7C38C)
Website satchelandcompass.com

Target Market(s)

location independent entrepreneurs, digital nomads, people looking to swap the 9 to 5 for a lifestyle business

Industry/Entity Type

Business

Contact Information for Business Card

Petra Varga
Your Lifestyle Business Coach, Retreat & Trip Leader
http://satchelandcompass.com
hello@satchelandcompass.com
Live a life you don't need a holiday from

Font styles to use
Serif
Sans Serif

Requirements
Must have
• One side should contain only the logo. I would also consider having the "Live a life you don't need a holiday from" on that side too (depending on how it looks)
• Please show both sides on the designs.

```html
<!DOCTYPE html>
<html lang="en">
<head>
<meta charset="utf-8">
<title>Satchel &amp; Compass — Business Card</title>
<link rel="stylesheet" href="https://fonts.googleapis.com/css2?family=Arimo:wght@400;700&display=swap">
<style>
  :root {
    --ink: #1b1b1b;
    --black: #000000;
    --green: #25a796;
    --green-band: #33ad9b;
    --sand: #d7c38c;
    --paper: #ffffff;
    --backdrop: #e6e6e6;
  }
  * { box-sizing: border-box; margin: 0; padding: 0; }
  html, body {
    width: 1189px; height: 1200px; overflow: hidden;
    background: var(--backdrop);
    font-family: "Arimo", Arial, sans-serif;
    color: var(--ink);
  }
  .card {
    position: absolute; left: 194px;
    width: 807px; height: 460px;
    background: var(--paper);
    box-shadow: 0 3px 8px rgba(0,0,0,0.25);
  }
  .card--front { top: 112px; }
  .card--back { top: 620px; }

  .wordmark {
    position: absolute;
    font-weight: 700;
    color: var(--black);
    letter-spacing: 0.5px;
    white-space: nowrap;
  }
  .card--front .wordmark {
    left: 0; right: 0; top: 128px;
    text-align: center; font-size: 50px;
  }
  .tagline {
    position: absolute; left: 0; right: 0; top: 354px;
    text-align: center; font-size: 19px; color: var(--black);
  }

  .card--back .wordmark {
    left: 37px; top: 62px; font-size: 33px;
  }
  .name-panel {
    position: absolute; left: 499px; top: 38px;
    width: 308px; height: 93px;
    background: var(--green);
    padding: 8px 14px;
  }
  .name-panel__name {
    font-size: 26px; font-weight: 700; color: var(--ink); line-height: 1.1;
  }
  .name-panel__role {
    font-size: 16px; color: var(--paper); line-height: 1.35; margin-top: 3px;
  }

  .photo-band {
    position: absolute; left: 0; top: 185px;
    width: 807px; height: 181px;
    background: var(--green-band);
  }
  .photo {
    position: absolute; top: 12px; height: 157px;
  }
  .photo--tower { left: 45px; width: 175px;
    background: linear-gradient(180deg, #b9d3ea 0%, #9aa0a4 55%, #6e5e52 100%); }
  .photo--sunset { left: 229px; width: 171px;
    background: linear-gradient(180deg, #d86aa6 0%, #ee8cc0 55%, #f2a35a 85%, #2a2424 100%); }
  .photo--cove { left: 410px; width: 172px;
    background: linear-gradient(180deg, #3f5fb2 0%, #5b7a3c 40%, #b9b4a4 65%, #2f8d6a 100%); }
  .photo--shore { left: 591px; width: 171px;
    background: linear-gradient(180deg, #dfe1e3 0%, #8d9c94 40%, #c69a78 70%, #4c5a3a 100%); }

  .contact {
    position: absolute; top: 397px;
    display: flex; align-items: center; gap: 12px;
    font-size: 17px; color: var(--ink);
  }
  .contact--email { left: 72px; }
  .contact--web { left: 459px; }
  .contact__icon { width: 24px; height: 24px; display: block; }
</style>
</head>
<body>

<section class="card card--front" aria-label="Card front">
  <div class="wordmark">Satchel &amp; Compass</div>
  <p class="tagline">Live a life you don't need a holiday from</p>
</section>

<section class="card card--back" aria-label="Card back">
  <div class="wordmark">Satchel &amp; Compass</div>

  <div class="name-panel">
    <div class="name-panel__name">Petra Varga</div>
    <div class="name-panel__role">Your Lifestyle Business Coach,<br>Retreat &amp; Trip Leader</div>
  </div>

  <div class="photo-band">
    <div class="photo photo--tower" role="img" aria-label="Photo of an old stone tower on rocks under a blue sky"></div>
    <div class="photo photo--sunset" role="img" aria-label="Photo of a pink sunset sky behind dark trees"></div>
    <div class="photo photo--cove" role="img" aria-label="Photo of a green cove with white cliffs and forested hills"></div>
    <div class="photo photo--shore" role="img" aria-label="Photo of a beach at low tide with a rainbow and palm trees"></div>
  </div>

  <div class="contact contact--email">
    <svg class="contact__icon" viewBox="0 0 24 24" aria-hidden="true">
      <rect width="24" height="24" rx="3" fill="var(--green)"/>
      <rect x="5" y="7" width="14" height="10" fill="none" stroke="#fff" stroke-width="1.5"/>
      <path d="M5 7 L12 13 L19 7 M5 17 L10 12 M19 17 L14 12" fill="none" stroke="#fff" stroke-width="1.3"/>
    </svg>
    <span>hello@satchelandcompass.com</span>
  </div>

  <div class="contact contact--web">
    <svg class="contact__icon" viewBox="0 0 24 24" aria-hidden="true">
      <rect width="24" height="24" rx="3" fill="var(--green)"/>
      <circle cx="12" cy="12" r="6.5" fill="none" stroke="#fff" stroke-width="1.3"/>
      <ellipse cx="12" cy="12" rx="2.8" ry="6.5" fill="none" stroke="#fff" stroke-width="1.1"/>
      <path d="M5.5 12 H18.5 M6.5 9 H17.5 M6.5 15 H17.5" stroke="#fff" stroke-width="1"/>
    </svg>
    <span>http://satchelandcompass.com</span>
  </div>
</section>

</body>
</html>
```